Re-Branding

I would like a new "brand" which will incorporate my new photo. I do title insurance in California for Harborline Deed Assurance Corp. Could be used on business cards or flyers.

Target Market(s)

Real Estate Professionals, Attorneys, Mortgage Companies and Banks.

Contact Information for Business Card

High Gloss

Requirements
Must have
• My photo, my logo and my contact information.
Nice to have
• background that is appealing to clients
Should not have
• home email address

```html
<!DOCTYPE html>
<html lang="en">
<head>
<meta charset="UTF-8">
<title>Dana Ortega – Business Card</title>
<link rel="stylesheet" href="https://fonts.googleapis.com/css2?family=Libre+Bodoni:wght@500;600&family=Montserrat:wght@500;600&display=swap">
<style>
  :root {
    --green: #138a3a;
    --navy: #14285a;
    --paper: #f4f4f2;
    --backdrop: #dcdcda;
    --photo-top: #d9c7a8;
    --photo-bottom: #1a8a3e;
  }
  * { margin: 0; padding: 0; box-sizing: border-box; }
  html, body { width: 1200px; height: 1170px; overflow: hidden; }
  body {
    background: var(--backdrop);
    font-family: "Montserrat", sans-serif;
    position: relative;
  }
  .card {
    position: absolute;
    left: 220px;
    width: 760px;
    height: 434px;
    background: var(--paper);
    overflow: hidden;
    box-shadow: 0 6px 18px rgba(0,0,0,0.12);
  }
  .card--back { top: 110px; }
  .card--front { top: 626px; }
  .card__shapes { position: absolute; inset: 0; width: 100%; height: 100%; }
  .card__shapes polygon { fill: var(--green); }

  .brand {
    position: absolute;
    display: flex;
    align-items: center;
    gap: 9px;
  }
  .brand__dot {
    width: 22px; height: 22px; border-radius: 50%;
    background: var(--green);
  }
  .brand__name {
    font-family: "Montserrat", sans-serif;
    font-weight: 600;
    font-size: 15px;
    color: var(--navy);
  }

  /* back */
  .back__title {
    position: absolute;
    top: 160px; left: 0; right: 0;
    text-align: center;
    color: #fff;
  }
  .back__name {
    font-family: "Libre Bodoni", serif;
    font-weight: 500;
    font-size: 52px;
    line-height: 1;
  }
  .back__role {
    margin-top: 8px;
    font-size: 17px;
    font-weight: 500;
    letter-spacing: 0.3px;
  }
  .card--back .brand { left: 0; right: 0; justify-content: center; top: 375px; }

  /* front */
  .front__info { position: absolute; left: 88px; top: 146px; color: var(--navy); }
  .front__name {
    font-family: "Libre Bodoni", serif;
    font-weight: 600;
    font-size: 56px;
    line-height: 1;
  }
  .front__role {
    margin-top: 8px;
    font-size: 17px;
    font-weight: 500;
    padding-bottom: 8px;
    border-bottom: 2px solid var(--green);
    width: 370px;
  }
  .front__phone {
    margin-top: 26px;
    font-family: "Libre Bodoni", serif;
    font-weight: 600;
    font-size: 36px;
    margin-left: 12px;
  }
  .front__contact { margin-left: 16px; font-size: 16px; font-weight: 500; line-height: 1.3; }
  .card--front .brand { left: 146px; top: 385px; }
  .front__photo {
    position: absolute;
    left: 445px; top: 62px;
    width: 230px; height: 372px;
    background: linear-gradient(180deg, var(--photo-top) 0%, var(--photo-top) 38%, var(--photo-bottom) 44%, var(--photo-bottom) 100%);
    border-radius: 90px 90px 0 0;
  }
</style>
</head>
<body>
  <section class="card card--back">
    <svg class="card__shapes" viewBox="0 0 760 434" preserveAspectRatio="none" aria-hidden="true">
      <polygon points="0,0 760,0 760,280 114,332 0,282"/>
    </svg>
    <div class="back__title">
      <div class="back__name">Dana Ortega</div>
      <div class="back__role">account executive | vice president</div>
    </div>
    <div class="brand">
      <span class="brand__dot"></span>
      <span class="brand__name">Harborline Deed Assurance Corp.</span>
    </div>
  </section>

  <section class="card card--front">
    <svg class="card__shapes" viewBox="0 0 760 434" preserveAspectRatio="none" aria-hidden="true">
      <polygon points="0,0 340,0 62,56 0,16"/>
      <polygon points="628,0 760,0 760,210 580,150"/>
      <polygon points="0,378 160,434 0,434"/>
    </svg>
    <div class="front__info">
      <div class="front__name">Dana Ortega</div>
      <div class="front__role">account executive | vice president</div>
      <div class="front__phone">555 014 2290</div>
      <div class="front__contact">
        <div>DOrtega@hdac.com</div>
        <div>Dana.HarborlineIE.com</div>
      </div>
    </div>
    <div class="front__photo" role="img" aria-label="Portrait photo of the account executive in a green top"></div>
    <div class="brand">
      <span class="brand__dot"></span>
      <span class="brand__name">Harborline Deed Assurance Corp.</span>
    </div>
  </section>
</body>
</html>
```